New business Cards

We need some new cards that stand out. We love our logo and colour scheme but need to incorporate a numo logo and ptl logo yet still keep our cards uncluttered and clean looking.
Our tag is Keen Ledgerworks. Anywhere, Anytime.
The idea of the cards is to show authority in accounting and Numo/ cloud software

```html
<!DOCTYPE html>
<html lang="en">
<head>
<meta charset="utf-8">
<title>Marlow Business Solutions – Business Cards</title>
<link rel="stylesheet" href="https://fonts.googleapis.com/css2?family=Didact+Gothic&family=Open+Sans:wght@400;600&display=swap">
<style>
  :root {
    --bg: #e9e7e3;
    --ink: #0f0f10;
    --ink-soft: #1c1c1e;
    --paper: #ffffff;
    --green: #6dbd4a;
    --green-deep: #4f9a35;
    --grey: #a7a9ac;
    --white: #ffffff;
    --badge-teal: #1fa9d6;
    --badge-sky: #28b6e0;
    --badge-blue: #1d57a6;
    --badge-gold: #f2c230;
  }
  * { box-sizing: border-box; margin: 0; padding: 0; }
  html, body { width: 1200px; height: 784px; overflow: hidden; }
  body {
    background: var(--bg);
    font-family: "Open Sans", Arial, sans-serif;
    position: relative;
  }
  .card {
    position: absolute;
    top: 237px;
    width: 540px;
    height: 309px;
    border-radius: 3px;
    overflow: hidden;
    box-shadow: 0 6px 18px rgba(0,0,0,.22);
  }
  .card--back {
    left: 40px;
    background: radial-gradient(ellipse at 50% 30%, var(--ink-soft), var(--ink) 75%);
  }
  .card--front { left: 620px; background: var(--ink); }

  .brand {
    display: flex;
    align-items: center;
    gap: 12px;
    color: var(--white);
    font-weight: 600;
  }
  .brand__mark { width: 42px; height: 42px; background: var(--green); flex: none; }
  .brand__name { font-size: 22px; line-height: 1.1; }

  .card--back .brand {
    position: absolute;
    left: 0; right: 0; top: 88px;
    justify-content: center;
  }
  .card--back .tagline {
    position: absolute;
    left: 0; right: 0; top: 226px;
    text-align: center;
    color: var(--green);
    font-family: "Didact Gothic", "Century Gothic", sans-serif;
    font-size: 15px;
    letter-spacing: 4px;
  }

  .front__top { position: absolute; left: 0; top: 0; width: 100%; height: 130px; background: var(--paper); }
  .front__top .brand { position: absolute; left: 34px; top: 44px; color: var(--ink); }
  .front__band {
    position: absolute; left: 0; top: 130px; width: 100%; height: 20px;
    background: var(--green);
    color: var(--ink);
    font-family: "Didact Gothic", "Century Gothic", sans-serif;
    font-size: 12px; letter-spacing: 3.5px;
    line-height: 20px;
    padding-left: 34px;
  }
  .person { position: absolute; left: 34px; top: 164px; }
  .person__name { color: var(--green); font-size: 17px; font-weight: 600; }
  .person__role { color: var(--grey); font-size: 13px; margin-top: 2px; }
  .contact { position: absolute; left: 34px; top: 218px; list-style: none; }
  .contact li {
    display: flex; align-items: center; gap: 8px;
    color: var(--white); font-size: 13.5px; line-height: 20px;
  }
  .contact svg { width: 14px; height: 14px; flex: none; }
  .contact .plain { padding-left: 22px; }

  .badges { position: absolute; right: 30px; top: 162px; width: 96px; }
  .badges__row { display: flex; gap: 6px; justify-content: flex-end; }
  .badge-circle { width: 38px; height: 38px; border-radius: 50%; }
  .badge-circle--numo { background: var(--badge-teal); }
  .badge-circle--advisor { background: var(--badge-sky); }
  .badge-ptl {
    margin-top: 8px; margin-left: auto; width: 82px; height: 36px;
    background: linear-gradient(90deg, var(--badge-blue) 62%, var(--badge-gold) 62%);
  }
</style>
</head>
<body>
  <section class="card card--back" aria-label="Card back">
    <div class="brand">
      <span class="brand__mark"></span>
      <span class="brand__name">Marlow Business Solutions</span>
    </div>
    <p class="tagline">KEEN LEDGERWORKS. ANYWHERE, ANYTIME.</p>
  </section>

  <section class="card card--front" aria-label="Card front">
    <div class="front__top">
      <div class="brand">
        <span class="brand__mark"></span>
        <span class="brand__name">Marlow Business Solutions</span>
      </div>
    </div>
    <div class="front__band">KEEN LEDGERWORKS. ANYWHERE, ANYTIME.</div>

    <div class="person">
      <p class="person__name">Elena Marlow, PTL, CTA</p>
      <p class="person__role">Partner</p>
    </div>

    <ul class="contact">
      <li>
        <svg viewBox="0 0 24 24" aria-hidden="true"><path fill="#6dbd4a" d="M6.6 10.8a15.1 15.1 0 0 0 6.6 6.6l2.2-2.2a1 1 0 0 1 1-.25 11.4 11.4 0 0 0 3.6.57 1 1 0 0 1 1 1V20a1 1 0 0 1-1 1A17 17 0 0 1 3 4a1 1 0 0 1 1-1h3.5a1 1 0 0 1 1 1c0 1.25.2 2.45.57 3.6a1 1 0 0 1-.25 1z"/></svg>
        03 5550 1829
      </li>
      <li>
        <svg viewBox="0 0 24 24" aria-hidden="true"><rect x="2" y="5" width="20" height="14" rx="1.5" fill="#6dbd4a"/><path d="M3 6.5l9 6.5 9-6.5" fill="none" stroke="#0f0f10" stroke-width="1.8"/></svg>
        elenam@marlowbussol.com.au
      </li>
      <li>
        <svg viewBox="0 0 24 24" aria-hidden="true"><g fill="none" stroke="#6dbd4a" stroke-width="2"><circle cx="12" cy="12" r="9"/><ellipse cx="12" cy="12" rx="4" ry="9"/><path d="M3 12h18"/></g></svg>
        www.marlowbussol.com.au
      </li>
      <li class="plain">Brindle Vic 3790</li>
    </ul>

    <div class="badges" aria-label="Partner badges">
      <div class="badges__row">
        <span class="badge-circle badge-circle--numo"></span>
        <span class="badge-circle badge-circle--advisor"></span>
      </div>
      <div class="badge-ptl"></div>
    </div>
  </section>
</body>
</html>
```